Lunaryth needs a elegant mystical business card design

The theme of Lunaryth is centered on Kemetic/Ancient Egyptian Spirituality. My business sells handmade scented candles, mystic oils, body sprays, tarot readings and more. I would like my business card to reflect an elegant and mystical look. Hieroglyphs around the borders would be a cool idea. Also, the main colors I am working with is Black and Gold= colors of royalty. Black background. The business card will be double sided. The back will have the logo, and the front will have the basic information (ie name, title, business, phone, email, website, etc..)

Target Market(s)

The target market are people into metaphysics, holistic healing, ancient Egyptian culture, aromatherapy, occult science, and the esoteric.

Industry/Entity Type

Business

Contact Information for Business Card

Name: Marisol T. Pike
Title: Owner
Business: LUNARYTH
Phone: 555.210.4473
Website: www.Lunaryth.example
Facebook, Instagram, and twitter icons

Font styles to use
Serif
Decorative

Requirements
Must have
• My logo, and website.
Nice to have
• Ancient Egyptian hieroglyphs, Elegant designs around the border, or encircling the logo.

```html
<!DOCTYPE html>
<html lang="en">
<head>
<meta charset="utf-8">
<title>Lunaryth — Business Card</title>
<link rel="stylesheet" href="https://fonts.googleapis.com/css2?family=Cinzel:wght@400;600&family=Alegreya:wght@400&display=swap">
<style>
  :root {
    --page: #e7e4df;
    --card-deep: #0a1311;
    --card-mid: #14211e;
    --glyph-tone: #1c2b27;
    --gold: #c9a86a;
    --gold-light: #e4cc95;
    --gold-dark: #8a6a36;
  }
  * { box-sizing: border-box; margin: 0; padding: 0; }
  html, body { width: 1200px; height: 800px; overflow: hidden; }
  body { background: var(--page); position: relative; font-family: "Alegreya", Georgia, serif; }

  .card {
    position: absolute;
    background: radial-gradient(ellipse at 60% 30%, var(--card-mid), var(--card-deep) 75%);
    box-shadow: 0 10px 30px rgba(0,0,0,.25);
    overflow: hidden;
  }

  /* Back (portrait, content turned a quarter) */
  .card-back { left: 110px; top: 100px; width: 350px; height: 600px; }
  .card-back-face {
    position: absolute; width: 600px; height: 350px;
    left: -125px; top: 125px; transform: rotate(90deg);
  }
  .glyph-field {
    position: absolute;
    background: repeating-linear-gradient(90deg, var(--glyph-tone) 0 26px, transparent 26px 34px);
    opacity: .55;
  }
  .card-back-face .glyph-field { inset: 14px; }

  .emblem {
    position: absolute;
    border-radius: 50%;
    background: radial-gradient(ellipse at center, rgba(201,168,106,.55), rgba(138,106,54,.25) 55%, transparent 72%);
  }
  .brand-name {
    position: absolute; left: 0; right: 0; text-align: center;
    font-family: "Cinzel", "Times New Roman", serif; font-weight: 600;
    color: var(--gold); letter-spacing: .12em;
  }
  .card-back-face .emblem { left: 130px; top: 40px; width: 340px; height: 260px; }
  .card-back-face .brand-name { top: 150px; font-size: 38px; }
  .card-back-face .website {
    position: absolute; left: 0; right: 0; bottom: 30px; text-align: center;
    font-size: 22px; color: var(--gold); letter-spacing: .12em;
  }

  /* Front (landscape) */
  .card-front { left: 530px; top: 210px; width: 620px; height: 360px; }
  .card-front .glyph-field { left: 14px; top: 150px; width: 420px; height: 196px; opacity: .4; }
  .card-front .emblem { left: 290px; top: 4px; width: 300px; height: 170px; }
  .card-front .brand-name { left: 290px; right: auto; width: 300px; top: 66px; font-size: 30px; }
  .flourish {
    position: absolute; height: 22px;
    background: linear-gradient(90deg, transparent, var(--gold-dark) 30%, var(--gold) 60%, transparent);
    border-radius: 11px; opacity: .8;
  }
  .flourish-left { left: 30px; top: 40px; width: 230px; }
  .flourish-right { left: 420px; top: 212px; width: 180px; }

  .contact { position: absolute; left: 150px; top: 168px; color: var(--gold); }
  .contact-name { font-family: "Cinzel", "Times New Roman", serif; font-weight: 600; font-size: 24px; letter-spacing: .06em; color: var(--gold-light); }
  .contact-title { font-family: "Cinzel", "Times New Roman", serif; font-size: 11px; letter-spacing: .2em; margin: 2px 0 8px 40px; }
  .contact-line { font-size: 19px; letter-spacing: .08em; line-height: 1.45; }
  .social { display: flex; gap: 6px; margin: 6px 0 4px; }
  .social-slot { width: 20px; height: 20px; border-radius: 4px; background: var(--gold); }
</style>
</head>
<body>

  <section class="card card-back" aria-label="Business card, back">
    <div class="card-back-face">
      <div class="glyph-field" role="img" aria-label="Faint border pattern of ancient Egyptian hieroglyphs"></div>
      <div class="emblem" role="img" aria-label="Gold winged emblem with ornamental scrolls around the brand name"></div>
      <div class="brand-name">LUNARYTH</div>
      <p class="website">www.Lunaryth.example</p>
    </div>
  </section>

  <section class="card card-front" aria-label="Business card, front">
    <div class="glyph-field" role="img" aria-label="Faint columns of ancient Egyptian hieroglyphs"></div>
    <div class="flourish flourish-left" role="img" aria-label="Gold ornamental scroll"></div>
    <div class="emblem" role="img" aria-label="Gold winged emblem with ornamental scrolls around the brand name"></div>
    <div class="brand-name">LUNARYTH</div>
    <div class="flourish flourish-right" role="img" aria-label="Gold ornamental scroll"></div>

    <div class="contact">
      <p class="contact-name">Marisol T. Pike</p>
      <p class="contact-title">OWNER</p>
      <p class="contact-line">555.210.4473</p>
      <p class="contact-line">marisol@lunaryth.example</p>
      <div class="social" aria-label="Social media profiles">
        <span class="social-slot"></span>
        <span class="social-slot"></span>
        <span class="social-slot"></span>
      </div>
      <p class="contact-line">www.Lunaryth.example</p>
    </div>
  </section>

</body>
</html>
```